Post Card Design Bright Path Youth

We need a postcard design that will be mailed to all residents offering free pickups of donated clothing. Our foundation is called Bright Path Youth, we are a nonprofit charitable organization that provides meals and medical services to children in need in Honduras. Collecting unwanted second-hand clothing generates revenue that helps fund the mission and programs run by our foundation. We would like to offer our pickup services to everyone who has any unwanted reusable clothing.

```html
<!DOCTYPE html>
<html lang="en">
<head>
<meta charset="utf-8">
<title>Bright Path Youth – Clothing Donation Postcard</title>
<link rel="stylesheet" href="https://fonts.googleapis.com/css2?family=Roboto:wght@400;700&display=swap">
<style>
  :root {
    --white: #ffffff;
    --ink: #1c1c1c;
    --green: #7cc242;
    --photo-light: #b8a795;
    --photo-mid: #7d6a57;
    --photo-dark: #1e1812;
    --box: #9a7a55;
  }
  * { margin: 0; padding: 0; box-sizing: border-box; }
  html, body { width: 800px; height: 1200px; overflow: hidden; background: var(--white); }
  .postcard {
    position: relative;
    width: 800px;
    height: 1200px;
    font-family: "Roboto", Arial, sans-serif;
    overflow: hidden;
  }
  .hero {
    position: absolute;
    inset: 0 0 auto 0;
    height: 1053px;
    background:
      radial-gradient(ellipse 55% 40% at 55% 38%, var(--photo-light) 0%, rgba(184,167,149,0) 70%),
      radial-gradient(ellipse 70% 30% at 45% 92%, var(--box) 0%, rgba(154,122,85,0) 75%),
      radial-gradient(ellipse 80% 70% at 50% 50%, var(--photo-mid) 0%, var(--photo-dark) 100%);
  }
  .headline {
    position: absolute;
    left: 80px;
    top: 218px;
    color: var(--white);
    font-weight: 700;
    font-size: 101px;
    line-height: 100px;
    letter-spacing: 1px;
    text-transform: uppercase;
  }
  .tagline {
    position: absolute;
    left: 79px;
    top: 832px;
    color: var(--white);
    font-weight: 400;
    font-size: 32px;
  }
  .footer {
    position: absolute;
    left: 0;
    right: 0;
    top: 1053px;
    bottom: 0;
    background: var(--white);
  }
  .pickup-note {
    position: absolute;
    left: 81px;
    top: 42px;
    font-size: 24px;
    font-weight: 400;
    color: var(--ink);
  }
  .phone-line {
    position: absolute;
    left: 80px;
    top: 72px;
    font-size: 43px;
    font-weight: 700;
    color: var(--green);
    letter-spacing: 1px;
  }
  .brand {
    position: absolute;
    left: 640px;
    top: 32px;
    width: 130px;
    text-align: center;
    color: var(--green);
    font-weight: 700;
    font-size: 17px;
    line-height: 20px;
  }
  .brand-dot {
    display: block;
    width: 34px;
    height: 34px;
    margin: 0 auto 8px;
    border-radius: 50%;
    background: var(--green);
  }
</style>
</head>
<body>
<main class="postcard">
  <div class="hero" role="img" aria-label="Photo of hands packing folded beige clothing into a cardboard donation box"></div>
  <h1 class="headline">Make a<br>difference<br>with your<br>unwanted<br>clothing</h1>
  <p class="tagline">Donate Today, Change a Child’s Tomorrow!</p>
  <footer class="footer">
    <p class="pickup-note">Arrange Your Free Pickup – It’s Quick and Easy!</p>
    <p class="phone-line">CALL: (201) 555-0148</p>
    <div class="brand"><span class="brand-dot"></span>Bright Path Youth</div>
  </footer>
</main>
</body>
</html>
```